2 Wine Label Designs

Amberly Cellars has been helping people give customized wine gifts since 1999. From large scale corporate clients, to 1 bottle personalized gifts, we offer a wide range of wines and templates for any occasion. Recently we’ve started to shift our focus to a younger demographic (21 to 35 year old women) and are in the process of updating our website and branding.

One big area we’re working to improve is the customizable wine label/engraving templates we offer on the site (to see our current template library go to www.amberlycellars.com/shop/wine, select a wine, choose “label” or “engraving” from the dropdown, and click “customize”). You’ll find that a lot of our current templates are outdated or aimed at an older demographic. Over the next few months we want to swap out most of these old templates with fun fresh designs.

We're asking designers to submit 2 customizable wine label templates for this project. One should be wedding themed and the other "Thank You" themed. Please see the attached PDF for more guidelines and creative direction.

Keep in mind, even if you aren't selected as the winner of this project we are going to go through and offer $50 for any label template submitted that we like ($100 if we want both). So there is a good chance you'll be getting some money for your work!

Please read though the attached guidelines PDF carefully (especially the "Must be Customizable" section).

Target Market(s)

21 to 35 year old women

Colors

Designer to choose colors to be used in the design.

Requirements
Must have
• See attached PDF
Nice to have
• See attached PDF
Should not have
• See attached PDF

```html
<!DOCTYPE html>
<html lang="en">
<head>
<meta charset="utf-8">
<title>Thank You Label Preview</title>
<link rel="stylesheet" href="https://fonts.googleapis.com/css2?family=Source+Sans+3:wght@400&family=Homemade+Apple&display=swap">
<style>
  :root {
    --page-bg: #ffffff;
    --ink: #1a1717;
    --cream: #f7f6dc;
    --leaf-dark: #1f6f55;
    --leaf-mid: #2f8a68;
    --leaf-light: #6fae5a;
    --shadow: rgba(0, 0, 0, 0.55);
  }
  * { margin: 0; padding: 0; box-sizing: border-box; }
  html, body {
    width: 1200px;
    height: 1000px;
    overflow: hidden;
    background: var(--page-bg);
  }
  .board {
    position: relative;
    width: 1200px;
    height: 1000px;
  }
  .board-caption {
    position: absolute;
    left: 42px;
    top: 124px;
    font-family: "Source Sans 3", sans-serif;
    font-size: 21px;
    line-height: 30px;
    color: var(--ink);
  }
  .wine-label {
    position: absolute;
    left: 360px;
    top: 151px;
    width: 529px;
    height: 681px;
    background: var(--cream);
    box-shadow: 5px 6px 6px var(--shadow);
  }
  .wine-label svg {
    position: absolute;
    inset: 0;
    width: 100%;
    height: 100%;
  }
  .label-greeting {
    position: absolute;
    left: 100px;
    top: 268px;
    width: 330px;
    text-align: center;
    font-family: "Homemade Apple", cursive;
    font-size: 46px;
    line-height: 1;
    color: var(--ink);
  }
</style>
</head>
<body>
  <main class="board">
    <p class="board-caption">Thank you.2 label<br>preview</p>

    <section class="wine-label">
      <svg viewBox="0 0 529 681" xmlns="http://www.w3.org/2000/svg">
        <defs>
          <linearGradient id="foliage-tone" x1="0" y1="0" x2="1" y2="1">
            <stop offset="0" stop-color="var(--leaf-mid)"/>
            <stop offset="0.5" stop-color="var(--leaf-dark)"/>
            <stop offset="1" stop-color="var(--leaf-light)"/>
          </linearGradient>
        </defs>
        <rect class="foliage-area" role="img"
              aria-label="Watercolour tropical palm fronds and monstera leaves filling the label"
              x="0" y="0" width="529" height="681" fill="url(#foliage-tone)" opacity="0.85"/>
        <path class="heart-panel" fill="var(--cream)"
              d="M250 219 C230 175 180 163 140 174 C90 189 64 240 71 300 C80 380 180 440 260 514 C330 440 430 380 440 290 C448 220 400 185 340 190 C300 194 266 208 250 219 Z"/>
      </svg>
      <p class="label-greeting">thank you</p>
    </section>
  </main>
</body>
</html>
```